I need a website built for my modeling agency company.

On our website, a user can create a profile and we will submit it to thousands of modeling agents throughout the country.

In many cases, they will receive multiple offers from modeling agencies which allows them to pick and choose the contract that is best for them to launch their modeling career.

Some tag lines to consider using:

"Submit your profile to hundreds of modeling agents instantly!"

"Get found and become a star!"

We are: The Runway Guild.

Our Slogan: The World''s Largest Network of Fashion Models and Agents

What We Do: We are an agency with one of the largest networks of fashion professionals that are looking for new modeling talent. We host professional profiles for aspiring models, professional fashion models seeking work, modeling talent seekers, and top modeling agencies. We connect aspiring models with the top modeling agencies in the United States and abroad.

By submitting your FREE profile, you will be instantly introduced to the industry’s leading modeling agents. Within a few days, you could receive multiple, competing offers from modeling agencies that all want to launch your modeling career. Receiving multiple signing offers puts you in control of deciding which contract best suites you!

Reason: I've seen some good designs, but none that are 100% perfect. These are the ones that I like best so far (to give you some ideas): http://files.pixelvane.example/img/510372/820114/820114_4917263_510372_image.jpg http://files.pixelvane.example/img/510372/829305/829305_4926851_510372_image.jpg http://files.pixelvane.example/img/510372/51847/51847_4924097_510372_image.jpg http://files.pixelvane.example/img/510372/51847/51847_4919856_510372_image.jpg http://files.pixelvane.example/img/510372/823670/823670_4920438_510372_image.jpg

Target Market(s)

Aspiring models (mostly female, but some male)

Industry/Entity Type

Modeling Agency

Colors

Designer to choose colors to be used in the design.

Requirements
Nice to have
• Somewhere in the top half of the page, I would like there to be a small form for the visitor to fill out. This form will look as follows:

Title: Instantly contact hundreds of modeling agents who are looking for new talent and could make you a star!
Fields: First Name*, Last Name*, Age, Zip Code, Email Address*, Daytime Phone, Evening Phone, Comments.

Then, there will be a "submit" button to proceed to next step of form. Just below the "submit" button, should be the following verbiage: "You will have the opportunity to upload photo(s) and provide other pertinent information in next step."

```html
<!DOCTYPE html>
<html lang="en">
<head>
<meta charset="utf-8">
<title>The Runway Guild</title>
<link rel="stylesheet" href="https://fonts.googleapis.com/css2?family=Roboto+Condensed:wght@400;700&family=Tinos&family=Playfair+Display&display=swap">
<style>
  :root {
    --black: #000;
    --panel: #1c1c1c;
    --footer: #222;
    --red: #ee1c24;
    --white: #fff;
    --sepia-light: #d9cbb0;
    --sepia-dark: #6b5a40;
  }
  * { box-sizing: border-box; margin: 0; padding: 0; }
  html, body { width: 853px; height: 1200px; overflow: hidden; background: var(--black); }
  body { position: relative; font-family: "Roboto Condensed", Arial, sans-serif; color: var(--white); }
  .abs { position: absolute; }

  .brand { left: 102px; top: 34px; display: flex; align-items: center; gap: 8px; }
  .brand-mark { width: 22px; height: 22px; background: var(--red); }
  .brand-name { font-family: "Playfair Display", Georgia, serif; font-size: 25px; color: var(--white); white-space: nowrap; }

  .account-links { right: 98px; top: 16px; font-size: 14px; letter-spacing: .2px; }
  .account-links span { margin: 0 6px; }

  .main-nav { left: 460px; top: 78px; display: flex; height: 25px; }
  .main-nav a { color: var(--white); text-decoration: none; font-size: 14px; line-height: 25px; padding: 0 8px; }
  .main-nav a.active { background: var(--red); }

  .hero { left: 95px; top: 103px; width: 665px; height: 222px;
    background: linear-gradient(100deg, var(--sepia-light) 0%, #bfae8c 35%, var(--sepia-dark) 70%, #3d3225 100%); }
  .hero-title { left: 186px; top: 154px; width: 252px; text-align: center; font-weight: 700; font-size: 22px; line-height: 31px; color: #111; text-transform: uppercase; }
  .btn-red { background: var(--red); color: var(--white); font-weight: 700; text-align: center; text-transform: uppercase; }
  .hero-signup { left: 244px; top: 265px; width: 76px; height: 29px; line-height: 29px; font-size: 16px; }

  .slogan-bar { left: 95px; top: 340px; width: 665px; height: 51px; background: var(--panel); }
  .slogan-bar p { text-align: center; line-height: 51px; font-weight: 700; font-size: 17px; }
  .slogan-bar svg { position: absolute; top: 16px; }

  .info-card { top: 412px; width: 188px; height: 214px; border: 2px solid var(--white); border-radius: 5px; background: var(--panel); padding: 8px 12px; }
  .info-card header { display: flex; align-items: center; gap: 8px; height: 38px; margin-bottom: 18px; }
  .info-card h2 { font-size: 13px; color: var(--red); font-weight: 700; }
  .info-card h2.light { font-weight: 400; font-size: 14px; }
  .info-card p { font-family: "Tinos", "Times New Roman", serif; font-size: 9.2px; line-height: 13.4px; }

  .gallery { left: 95px; top: 648px; width: 665px; height: 148px; background: var(--panel); }
  .gallery-title { left: 173px; top: 658px; font-size: 12.5px; font-weight: 700; color: var(--red); }
  .thumb { top: 688px; width: 93px; height: 88px; }
  .arrow-btn { width: 40px; height: 40px; border-radius: 50%; background: var(--black); top: 711px; }

  .upload-band { left: 95px; top: 818px; width: 665px; height: 119px; background: var(--red); }
  .upload-title { left: 179px; top: 824px; font-size: 22px; font-weight: 700; color: #111; }
  .upload-sub { left: 178px; top: 856px; width: 546px; text-align: center; font-size: 11.5px; line-height: 13px; font-weight: 700; color: #111; }
  .file-field { left: 180px; top: 893px; width: 402px; height: 32px; background: var(--white); color: #111; font-style: italic; font-size: 12.5px; line-height: 32px; padding-left: 36px; }
  .upload-btn { left: 599px; top: 893px; width: 127px; height: 32px; background: #111; line-height: 32px; text-align: center; font-weight: 700; font-size: 20px; }

  .field-label { font-size: 12px; font-weight: 700; }
  .field { background: var(--white); height: 23px; }
  .submit-btn { left: 486px; top: 1106px; width: 127px; height: 29px; line-height: 29px; font-size: 19px; color: #111; }
  .back-link { left: 631px; top: 1120px; font-size: 9.5px; }

  .site-footer { left: 0; top: 1148px; width: 853px; height: 52px; background: var(--footer); }
  .follow { left: 101px; top: 1162px; font-size: 12px; font-weight: 700; display: flex; align-items: center; gap: 10px; }
  .social-dot { width: 16px; height: 16px; border-radius: 50%; background: var(--white); }
  .footer-nav { left: 360px; top: 1164px; display: flex; gap: 10px; font-size: 8.5px; }
  .copyright { left: 0; width: 853px; top: 1182px; text-align: center; font-size: 7px; padding-left: 58px; }
  .footer-brand { left: 622px; top: 1160px; display: flex; align-items: center; gap: 6px; }
  .footer-brand .brand-mark { width: 14px; height: 14px; }
  .footer-brand .brand-name { font-size: 16px; }
</style>
</head>
<body>
  <div class="abs brand"><span class="brand-mark"></span><span class="brand-name">The Runway Guild</span></div>
  <div class="abs account-links">SIGN UP<span>|</span>LOG IN</div>
  <nav class="abs main-nav">
    <a class="active" href="#">HOME</a><a href="#">MODELS</a><a href="#">CASTING</a><a href="#">SPECIALS</a><a href="#">CONTACT</a>
  </nav>

  <div class="abs hero" role="img" aria-label="Sepia photo of two young models lying on their backs, smiling"></div>
  <h1 class="abs hero-title">"Submit your profile to hundreds of modeling agents instantly!"</h1>
  <div class="abs btn-red hero-signup">Sign up</div>

  <div class="abs slogan-bar">
    <svg style="left:20px" width="18" height="20" viewBox="0 0 18 20"><path d="M14 2 L5 10 L14 18" stroke="#fff" stroke-width="4" fill="none"/></svg>
    <p>THE WORLD''S LARGEST NETWORK OF FASHION MODELS AND AGENTS</p>
    <svg style="right:20px" width="18" height="20" viewBox="0 0 18 20"><path d="M4 2 L13 10 L4 18" stroke="#fff" stroke-width="4" fill="none"/></svg>
  </div>

  <section class="abs info-card" style="left:122px">
    <header>
      <svg width="36" height="36" viewBox="0 0 36 36"><path d="M2 4 L34 4 L18 34 Z" fill="#ee1c24"/><path d="M18 4 L18 20 M10 26 L18 20 L26 26" stroke="#1c1c1c" stroke-width="3" fill="none"/></svg>
      <h2>WHO WE ARE</h2>
    </header>
    <p>We are an agency with one of the largest networks of fashion professionals that are looking for new modeling talent. We host professional profiles for aspiring models, professional fashion models seeking work, modeling talent seekers, and top modeling agencies. We connect aspiring models with the top modeling agencies in the United States and abroad.</p>
  </section>
  <section class="abs info-card" style="left:335px">
    <header>
      <svg width="40" height="38" viewBox="0 0 40 38"><path d="M2 12 L20 20 L13 23 L19 34 L15 36 L9 25 L4 30 Z" fill="#ee1c24"/><path d="M22 9 Q22 2 29 2 Q36 2 36 9 Q36 13 31 15 L31 20" stroke="#ee1c24" stroke-width="4" fill="none"/><rect x="29" y="23" width="4" height="4" fill="#ee1c24"/></svg>
      <h2>WHY US?</h2>
    </header>
    <p>We are an agency with one of the largest networks of fashion professionals that are looking for new modeling talent. We host professional profiles for aspiring models, professional fashion models seeking work, modeling talent seekers, and top modeling agencies. We connect aspiring models with the top modeling agencies in the United States and abroad.</p>
  </section>
  <section class="abs info-card" style="left:545px">
    <header>
      <svg width="30" height="38" viewBox="0 0 30 38"><rect x="2" y="5" width="26" height="31" fill="none" stroke="#ee1c24" stroke-width="2"/><rect x="9" y="2" width="12" height="6" fill="#1c1c1c" stroke="#ee1c24" stroke-width="2"/><path d="M8 21 L13 27 L23 14" stroke="#ee1c24" stroke-width="2.5" fill="none"/></svg>
      <h2 class="light">WHAT WE DO</h2>
    </header>
    <p>We are an agency with one of the largest networks of fashion professionals that are looking for new modeling talent. We host professional profiles for aspiring models, professional fashion models seeking work, modeling talent seekers, and top modeling agencies. We connect aspiring models with the top modeling agencies in the United States and abroad.</p>
  </section>

  <div class="abs gallery"></div>
  <div class="abs gallery-title">GET FOUND AND BECOME A STAR</div>
  <div class="abs arrow-btn" style="left:116px"><svg width="40" height="40" viewBox="0 0 40 40"><path d="M23 12 L15 20 L23 28" stroke="#fff" stroke-width="4" fill="none"/></svg></div>
  <div class="abs thumb" style="left:167px;background:linear-gradient(135deg,#7a8fa0,#2a3540)" role="img" aria-label="Model portrait with blue eyeshadow"></div>
  <div class="abs thumb" style="left:275px;background:linear-gradient(135deg,#b58ad0,#4a2560)" role="img" aria-label="Model portrait in purple tones"></div>
  <div class="abs thumb" style="left:380px;background:linear-gradient(135deg,#6a6a6a,#111)" role="img" aria-label="Black and white model portrait"></div>
  <div class="abs thumb" style="left:487px;background:linear-gradient(135deg,#e0a070,#8a4a20)" role="img" aria-label="Smiling model portrait in warm tones"></div>
  <div class="abs thumb" style="left:595px;background:linear-gradient(135deg,#a05070,#2a0a15)" role="img" aria-label="Model portrait in dark red tones"></div>
  <div class="abs arrow-btn" style="left:700px"><svg width="40" height="40" viewBox="0 0 40 40"><path d="M17 12 L25 20 L17 28" stroke="#fff" stroke-width="4" fill="none"/></svg></div>

  <div class="abs upload-band"></div>
  <h2 class="abs upload-title">UPLOAD PHOTO</h2>
  <p class="abs upload-sub">INSTANTLY CONTACT HUNDREDS OF MODELING AGENTS WHO ARE LOOKING FOR NEW TALENT AND COULD MAKE YOU A STAR!</p>
  <div class="abs file-field">SELECT YOUR FILE</div>
  <div class="abs upload-btn">UPLOAD</div>

  <form>
    <label class="abs field-label" style="left:153px;top:948px">NAME:</label>
    <div class="abs field" style="left:138px;top:966px;width:281px"></div>
    <label class="abs field-label" style="left:151px;top:996px">AGE:</label>
    <div class="abs field" style="left:138px;top:1015px;width:281px"></div>
    <label class="abs field-label" style="left:151px;top:1041px">ZIP CODE:</label>
    <div class="abs field" style="left:138px;top:1062px;width:281px"></div>
    <label class="abs field-label" style="left:151px;top:1091px">EMAIL ADDRESS</label>
    <div class="abs field" style="left:136px;top:1110px;width:281px"></div>

    <label class="abs field-label" style="left:502px;top:948px">PHONE:</label>
    <div class="abs field" style="left:486px;top:966px;width:240px"></div>
    <label class="abs field-label" style="left:502px;top:996px">COMMENTS</label>
    <div class="abs field" style="left:486px;top:1014px;width:240px;height:79px"></div>

    <div class="abs btn-red submit-btn">SUBMIT</div>
    <div class="abs back-link">WAIT, GO BACK</div>
  </form>

  <footer class="abs site-footer"></footer>
  <div class="abs follow">FOLLOW US:<span class="social-dot"></span><span class="social-dot"></span></div>
  <div class="abs footer-nav"><span>HOME</span><span>MODELS</span><span>CASTING</span><span>SPECIALS</span><span>CONTACT</span></div>
  <div class="abs copyright">COPY-RIGHT@THE RUNWAY GUILD</div>
  <div class="abs footer-brand"><span class="brand-mark"></span><span class="brand-name">The Runway Guild</span></div>
</body>
</html>
```